I need a Movie Poster for a comedy called "G(R)ip Lowdown". The story is about a unsuccessful sloppy film producer who casts to traffic cops for a reality TV show. "Real action, true cases". The only problem is, they are traffic cops and don't have such cases. So they have to invent them. Followed by a young inexperienced guy with a camera, they start out to create the action needed for the show. The movie is planned for next Spring, so no footage has been shot at this point and no stills are available. The two cops start out as complete wanna be cool guys facing lots of roadblocks until they finally become the eros they want to be at the end of the story. - Possible Log Line: "Fake it until you make it".
Industry/Entity Type
Film Production
Requirements
Must have
- My first idea was two cool wannabe cops with a sloppy young camera guy following them along. I am open to ideas.

```html
<!DOCTYPE html>
<html lang="en">
<head>
<meta charset="utf-8">
<title>Grip Lowdown – Movie Poster</title>
<link rel="stylesheet" href="https://fonts.googleapis.com/css2?family=Bebas+Neue&family=Oswald:wght@400;600;700&family=Roboto+Condensed:wght@400;500;700&display=swap">
<style>
  :root {
    --sky-top: #e4e9ee;
    --sky-mid: #a9b6c4;
    --sky-low: #6c7f95;
    --night: #0d1624;
    --night-deep: #05090f;
    --navy: #142238;
    --white: #ffffff;
    --tape: #f5d310;
    --tape-edge: #1a1a1a;
    --rec-red: #e0201b;
    --flare-blue: #3f8cff;
    --flare-red: #ff3b3b;
    --silhouette: #0f1620;
    --credit: #d8dde4;
    --credit-soft: #9aa4b1;
  }
  * { margin: 0; padding: 0; box-sizing: border-box; }
  html, body { width: 849px; height: 1200px; overflow: hidden; background: var(--night-deep); }
  .poster {
    position: relative;
    width: 849px;
    height: 1200px;
    overflow: hidden;
    background: linear-gradient(180deg, var(--sky-top) 0%, var(--sky-mid) 40%, var(--sky-low) 62%, var(--night) 74%, var(--night-deep) 100%);
  }
  .tagline {
    position: absolute;
    top: 22px;
    left: 0;
    width: 100%;
    text-align: center;
    font-family: "Roboto Condensed", sans-serif;
    font-weight: 500;
    font-size: 50px;
    color: var(--navy);
    letter-spacing: 0.5px;
  }
  .tagline .accent { color: var(--white); }
  .cops-art {
    position: absolute;
    left: 60px;
    top: 120px;
    width: 720px;
    height: 800px;
    background:
      radial-gradient(ellipse 30% 46% at 32% 52%, var(--silhouette) 0%, var(--silhouette) 62%, rgba(15,22,32,0) 100%),
      radial-gradient(ellipse 30% 50% at 68% 48%, var(--silhouette) 0%, var(--silhouette) 62%, rgba(15,22,32,0) 100%);
  }
  .viewfinder { position: absolute; left: 0; top: 0; }
  .rec {
    position: absolute;
    top: 128px;
    left: 728px;
    font-family: "Roboto Condensed", sans-serif;
    font-weight: 500;
    font-size: 30px;
    color: var(--navy);
    display: flex;
    align-items: center;
    gap: 8px;
  }
  .rec .dot { width: 24px; height: 24px; border-radius: 50%; background: var(--rec-red); }
  .tape {
    position: absolute;
    background: var(--tape);
    border-top: 3px solid var(--tape-edge);
    border-bottom: 3px solid var(--tape-edge);
    font-family: "Oswald", sans-serif;
    font-weight: 700;
    color: #111;
    white-space: nowrap;
    display: flex;
    align-items: center;
    box-shadow: 0 4px 10px rgba(0,0,0,0.35);
  }
  .tape-upper {
    left: 60px; top: 470px; width: 860px; height: 66px;
    font-size: 46px; padding-left: 60px;
    transform: rotate(-5deg);
  }
  .tape-lower {
    left: -60px; top: 600px; width: 960px; height: 60px;
    font-size: 42px; padding-left: 70px;
    transform: rotate(-9deg);
  }
  .lights { position: absolute; left: 0; top: 860px; width: 849px; height: 120px; }
  .flare { position: absolute; top: 20px; width: 180px; height: 60px; border-radius: 50%; }
  .flare-white { left: 180px; background: radial-gradient(ellipse, #ffffff 0%, rgba(255,255,255,0.5) 25%, transparent 70%); }
  .flare-blue { left: 335px; background: radial-gradient(ellipse, #ffffff 0%, var(--flare-blue) 25%, transparent 70%); }
  .flare-red { left: 490px; background: radial-gradient(ellipse, #ffffff 0%, var(--flare-red) 25%, transparent 70%); }
  .title {
    position: absolute;
    top: 935px;
    width: 100%;
    text-align: center;
    font-family: "Bebas Neue", sans-serif;
    font-weight: 400;
    font-size: 128px;
    line-height: 1;
    letter-spacing: 8px;
    color: var(--white);
  }
  .credits {
    position: absolute;
    top: 1066px;
    left: 0;
    width: 100%;
    text-align: center;
    font-family: "Oswald", sans-serif;
    font-weight: 400;
    font-size: 12px;
    line-height: 1.8;
    color: var(--credit);
    text-transform: uppercase;
  }
  .credits .line { display: block; white-space: nowrap; }
  .credits small { font-size: 7px; color: var(--credit-soft); }
</style>
</head>
<body>
<main class="poster">
  <h2 class="tagline">Fake It <span class="accent">Until</span> You Make It</h2>

  <div class="cops-art" role="img" aria-label="Illustration of two police officers in silhouette, standing back to back with pistols raised"></div>

  <svg class="viewfinder" width="849" height="1200" viewBox="0 0 849 1200" aria-hidden="true">
    <g fill="none" stroke="#ffffff" stroke-width="5">
      <path d="M30 170 V110 H92"/>
      <path d="M757 110 H819 V170"/>
      <path d="M30 790 V850 H92"/>
      <path d="M757 850 H819 V790"/>
    </g>
    <g stroke="#ffffff" stroke-width="3">
      <line x1="425" y1="488" x2="425" y2="532"/>
      <line x1="403" y1="510" x2="447" y2="510"/>
    </g>
  </svg>

  <div class="rec">REC <span class="dot"></span></div>

  <div class="tape tape-lower">CRIME SCENE&nbsp;&nbsp;&nbsp;&nbsp;DO NOT CROSS&nbsp;&nbsp;&nbsp;&nbsp;CRIME SCENE</div>
  <div class="tape tape-upper">CRIME SCENE DO NOT CROSS&nbsp;&nbsp;&nbsp;CRIME</div>

  <div class="lights" aria-hidden="true">
    <span class="flare flare-white"></span>
    <span class="flare flare-blue"></span>
    <span class="flare flare-red"></span>
  </div>

  <h1 class="title">GRIP LOWDOWN</h1>

  <p class="credits">
    <span class="line">Studio Name Pictures <small>presents</small> Producers <small>a film by</small> Script Writer Actor One Actor Two "Movie Title"</span>
    <span class="line"><small>music</small> The Musician Jodi Designer Name <small>edited by</small> Editors Name <small>production</small> Designers Name <small>photo</small> Cinematographer</span>
    <span class="line"><small>produced</small> Ex Producer 1 Ex Producer 2 <small>and</small> Producer One Producer 2 <small>story</small> Story Writer</span>
    <span class="line"><small>written by</small> Screen Writer <small>directed by</small> Director Name</span>
  </p>
</main>
</body>
</html>
```